Website Design for Stratolift As a Service

We are building a service to allow customers to own their own private clouds easily and cheaply. Owning your own private cloud saves costs, and offers more flexibility than a public cloud provider but has historically been a complex and expensive option.

We plan to offer a service where we build and maintain your own private cloud on your own hardware for a cheap monthly costs. Similar to this service - https://stackorra.com/solutions/private-cloud

We already have a logo and branding in place - we'd like a website design to be tailored from this branding, see attached logo design.

Feel free to add important elements on the home page such as testimonials, client/partner logos, contact form, social media, etc using placeholder contents in addition to the document we attached.

We also plan to add sub-pages in the future so please make sure that your website design has a full navigation menu.

An example of the site we like: https://www.verimoxa.com/ we'd be happy for you to take inspiration from this website.

Target Market(s)

B2B focused, we are targeting start-up/small/medium sized companies who needs help with their cloud and IT infrastructure.

Industry/Entity Type

IT

Number of Pages Required

1 page

Font styles to use
Other font styles liked:
• Please refer to the attachment - font must have Mayeka Demi Bold & Retroica

Requirements
Must have
• Please add placeholder menu since we're planning to have subpages later on.

```html
<!DOCTYPE html>
<html lang="en">
<head>
<meta charset="utf-8">
<title>Stratolift — Private Cloud as a Service</title>
<link href="https://fonts.googleapis.com/css2?family=Poppins:wght@400;500;600;700&display=swap" rel="stylesheet">
<style>
:root{
  --navy:#0e2a45;
  --navy-deep:#0a2035;
  --blue:#1f86d2;
  --blue-bright:#2ea3ee;
  --ink:#2b2b2b;
  --muted:#666b72;
  --white:#ffffff;
  --red:#e0153a;
}
*{box-sizing:border-box;margin:0;padding:0}
html,body{width:1200px;height:4292px;overflow:hidden}
body{font-family:"Poppins",sans-serif;color:var(--ink);background:var(--white);position:relative}
.abs{position:absolute}
a{color:inherit;text-decoration:none}

.topbar{left:0;top:0;width:1200px;height:37px;background:var(--navy);color:#cfd8e2;font-size:11px;text-align:center;line-height:37px}
.social{display:flex;gap:10px;align-items:center}
.social span{display:block;width:12px;height:12px;border-radius:50%;background:#fff}
.topbar .social{position:absolute;right:60px;top:12px}

.nav{left:0;top:37px;width:1200px;height:60px;background:#fff}
.brand{display:flex;align-items:center;gap:10px;font-weight:600;font-size:32px;color:var(--blue);letter-spacing:-.5px;white-space:nowrap}
.brand i{display:block;width:40px;height:40px;border-radius:50%;background:var(--blue)}
.nav .brand{left:60px;top:8px}
.menu{left:453px;top:21px;display:flex;font-size:13px;font-weight:500;color:#222}
.menu a{margin-right:26px}
.login{left:913px;top:21px;font-size:13px;font-weight:500;display:flex;gap:8px;align-items:center}
.search{left:868px;top:18px}
.btn{display:inline-block;border-radius:20px;font-size:13px;font-weight:500;text-align:center}
.btn-blue{background:var(--blue);color:#fff}
.btn-white{background:#fff;color:var(--blue)}
.sales{left:1012px;top:13px;width:128px;height:37px;line-height:37px}

.hero{left:0;top:97px;width:1200px;height:540px;background:var(--navy)}
.hero h1{left:62px;top:80px;width:560px;font-size:33px;line-height:45px;font-weight:600;color:#fff}
.hero h1 em{font-style:normal;color:var(--blue-bright)}
.hero p{left:62px;top:222px;width:550px;font-size:12.5px;line-height:23px;color:#e4ecf4}
.hero .btn{left:62px;top:326px;width:116px;height:35px;line-height:35px}
.hero-art{left:658px;top:65px;width:417px;height:333px;border-radius:30px;background:radial-gradient(ellipse at 50% 55%,#2bb5f2 0%,#1a6fb0 40%,#143e63 70%,#0e2a45 100%)}

.sec-title{width:1200px;left:0;text-align:center;font-size:26px;font-weight:600;color:var(--blue)}

.card{width:340px;height:250px;background:#fff;border-radius:6px;box-shadow:0 2px 14px rgba(20,40,70,.10);text-align:center}
.card .ico{position:absolute;left:125px;top:31px;width:90px;height:90px;border-radius:50%;border:2px solid #d3e6f6;background:radial-gradient(circle,#cfe6f8 0 55%,#fff 56%)}
.card h3{position:absolute;left:20px;right:20px;top:137px;font-size:16px;font-weight:500;color:var(--blue);line-height:24px}
.card p{position:absolute;left:30px;right:30px;font-size:12.5px;line-height:22px;color:var(--muted)}

.band{left:0;top:1348px;width:1200px;height:457px;background:var(--blue);color:#fff;overflow:hidden}
.band h2{left:62px;top:42px;width:560px;font-size:26px;line-height:44px;font-weight:600}
.band .copy{left:62px;top:140px;width:590px;font-size:12.5px;line-height:22px;color:#eaf4fc}
.band .copy p{margin-bottom:14px}
.band .btn{left:60px;top:369px;width:118px;height:34px;line-height:34px}
.feat{left:723px;display:flex;align-items:center;gap:22px;font-size:16px;font-weight:500}
.feat .dot{width:60px;height:60px;border-radius:50%;background:#fff;display:flex;align-items:center;justify-content:center}

.partner{display:flex;align-items:center;gap:10px;font-size:26px;font-weight:600;color:var(--navy);transform:translateX(-50%);white-space:nowrap}
.partner i{display:block;width:28px;height:28px;border-radius:50%;background:var(--blue)}

.pub-art{left:0;top:2113px;width:502px;height:464px;background:linear-gradient(160deg,#6d6e6f,#505253)}
.pub-bg{left:502px;top:2113px;width:698px;height:464px;background:#f4f6f8}
.pub h2{left:537px;top:2158px;font-size:25px;font-weight:600;color:var(--blue)}
.pub .copy{left:537px;top:2207px;width:600px;font-size:12.5px;line-height:22.5px;color:var(--muted)}
.pub .copy p{margin-bottom:13px}
.pub .btn{left:533px;top:2483px;width:102px;height:35px;line-height:35px}

.diff{left:0;top:2577px;width:1200px;height:433px;background:var(--blue);color:#fff}
.diff h2{left:62px;top:50px;font-size:26px;font-weight:600}
.diff ul{left:62px;top:100px;width:590px;list-style:none;font-size:12.5px;line-height:22px}
.diff li{position:relative;padding-left:22px;margin-bottom:6px}
.diff li svg{position:absolute;left:0;top:4px}
.diff-art{left:733px;top:40px;width:417px;height:350px;border-radius:24px;background:linear-gradient(150deg,#6cc6f5 0%,#3aa5e6 50%,#2b8fd7 100%)}

.tcard{top:3193px;width:318px;height:265px;background:#fff;box-shadow:0 2px 14px rgba(20,40,70,.10);text-align:center}
.tcard.active{background:var(--blue);color:#fff;box-shadow:none}
.tcard .q{position:absolute;left:127px;top:-32px;width:64px;height:64px;border-radius:50%;background:var(--blue);border:4px solid #fff;display:flex;align-items:center;justify-content:center}
.tcard p{position:absolute;left:30px;right:30px;top:58px;font-size:12.5px;line-height:22.5px;color:var(--muted)}
.tcard.active p,.tcard.active .role{color:#fff}
.tcard .who{position:absolute;left:0;right:0;top:188px;font-size:16px;font-weight:500;color:var(--blue)}
.tcard.active .who{color:#fff}
.tcard .role{position:absolute;left:0;right:0;top:215px;font-size:12.5px;color:var(--muted)}
.tail{position:absolute;right:40px;bottom:-26px}

.footer-bg{left:0;top:3930px;width:1200px;height:362px;background:var(--navy)}
.form{left:300px;top:3630px;width:600px;height:373px;background:var(--blue);border-radius:10px;color:#fff}
.form .lead{position:absolute;left:0;right:0;top:33px;text-align:center;font-size:12px}
.field{position:absolute;background:#fff;height:35px;font-size:11.5px;color:#888;padding:9px 12px}
.form .btn{position:absolute;left:255px;top:313px;width:90px;height:34px;line-height:34px;color:var(--ink)}

.foot-brand{left:60px;top:4050px}
.foot-brand .brand{font-size:28px}
.foot-brand .brand i{width:34px;height:34px}
.foot-about{left:60px;top:4100px;width:240px;font-size:11.5px;line-height:20px;color:#d7e0ea}
.fhead{font-size:14px;font-weight:600;color:var(--blue-bright)}
.flinks{font-size:11.5px;color:#fff;line-height:29px}
.contact-row{display:flex;gap:14px;align-items:flex-start;font-size:11.5px;color:#fff;line-height:18px}
.news-in{left:865px;top:4133px;width:243px;height:35px;background:#fff;font-size:11.5px;color:#333;padding:9px 14px}
.news-go{left:1108px;top:4133px;width:34px;height:35px;background:var(--red);display:flex;align-items:center;justify-content:center}
.bottombar{left:0;top:4262px;width:1200px;height:30px;background:var(--navy-deep);text-align:center;font-size:11px;line-height:30px;color:#dfe6ee}
.bottombar b{color:var(--blue-bright);font-weight:400}
.bottombar .social{position:absolute;right:60px;top:9px}
</style>
</head>
<body>

<div class="abs topbar">Lorem Ipsum is simply dummy text of the printing.
  <div class="social" aria-label="Social links"><span></span><span></span><span></span><span></span></div>
</div>

<header class="abs nav">
  <div class="abs brand"><i></i>Stratolift</div>
  <nav class="abs menu"><a href="#">Products</a><a href="#">Solutions</a><a href="#">Pricing</a><a href="#">Resources</a><a href="#">About</a></nav>
  <svg class="abs search" width="22" height="22" viewBox="0 0 22 22" fill="none" stroke="#222" stroke-width="2"><circle cx="9" cy="9" r="6"/><path d="M14 14l5 5"/></svg>
  <div class="abs login"><svg width="16" height="16" viewBox="0 0 16 16" fill="none" stroke="#222" stroke-width="1.5"><circle cx="8" cy="5" r="3"/><path d="M2 15c0-3.5 2.7-5.5 6-5.5s6 2 6 5.5"/></svg>Log In</div>
  <a class="abs btn btn-blue sales" href="#">Talk To Sales</a>
</header>

<section class="abs hero">
  <h1 class="abs">A groundbreaking way for your small business to <em>benefit from the power of the cloud</em></h1>
  <p class="abs">Stratolift as a Service is here to help small businesses utilise the power of the cloud without complicated set-ups or scary price tags. Ready to modernise your infrastructure with a fully managed private cloud solution from SCaaS?</p>
  <a class="abs btn btn-blue" href="#">Contact Us</a>
  <div class="abs hero-art" role="img" aria-label="Isometric illustration of a glowing infinity loop linking cloud servers and devices"></div>
</section>

<h2 class="abs sec-title" style="top:672px">How SCAAS benefits your business</h2>

<div class="abs card" style="left:60px;top:737px"><div class="ico" role="img" aria-label="Hands holding a cloud icon"></div><h3>Totally Flexible</h3><p style="top:168px">get the cloud you want and the latest innovations you need</p></div>
<div class="abs card" style="left:430px;top:737px"><div class="ico" role="img" aria-label="Stopwatch and gear icon"></div><h3>Faster</h3><p style="top:168px">our private cloud solutions outpace public clouds</p></div>
<div class="abs card" style="left:800px;top:737px"><div class="ico" role="img" aria-label="Money bag and coins icon"></div><h3>Greater value for money</h3><p style="top:168px">totally transparent pricing for no nasty month-end surprises</p></div>
<div class="abs card" style="left:60px;top:1013px"><div class="ico" role="img" aria-label="Hand holding a money bag icon"></div><h3>No consultancy fees</h3><p style="top:168px">we'll work with you and charge set fees for everything</p></div>
<div class="abs card" style="left:430px;top:1013px"><div class="ico" role="img" aria-label="Monitoring dashboard chart icon"></div><h3 style="top:133px">Management, monitoring and maintenance</h3><p style="top:190px">they're all included in your monthly price</p></div>
<div class="abs card" style="left:800px;top:1013px"><div class="ico" role="img" aria-label="Gear and cloud icon"></div><h3>Tried and tested cloud solutions</h3><p style="top:168px">we'll deploy the right OpenStratus solutions for your business</p></div>

<section class="abs band">
  <h2 class="abs">SCAAS can drive your digital transformation today</h2>
  <div class="abs copy">
    <p>Organisations of all shapes and sizes are reaping the time and money saving benefits that the cloud brings.</p>
    <p>But for small businesses seeking to transition, managing the time and financial costs of transitioning, and knowing whether to opt for a public or private cloud can cause you to hit the pause button.</p>
    <p>SCAAS is here to help you switch on your cloud transformation in a way that works best for you.&nbsp; We deliver and support fully managed private cloud solutions that are:</p>
  </div>
  <a class="abs btn btn-white" href="#">Get started</a>
  <div class="abs feat" style="top:57px"><div class="dot"><svg width="30" height="30" viewBox="0 0 30 30" fill="none" stroke="#1f86d2" stroke-width="2"><circle cx="15" cy="17" r="10"/><path d="M15 17V11M12 4h6"/></svg></div>Fast</div>
  <div class="abs feat" style="top:142px"><div class="dot"><svg width="30" height="30" viewBox="0 0 30 30" fill="none" stroke="#1f86d2" stroke-width="2"><rect x="8" y="4" width="14" height="22" rx="2"/><path d="M13 22h4"/></svg></div>Easy</div>
  <div class="abs feat" style="top:224px"><div class="dot"><svg width="30" height="30" viewBox="0 0 30 30" fill="none" stroke="#1f86d2" stroke-width="2"><path d="M17 4l-7 12h6l-3 10 8-13h-6z"/></svg></div>Powerful</div>
  <div class="abs feat" style="top:305px"><div class="dot"><svg width="30" height="30" viewBox="0 0 30 30" fill="none" stroke="#1f86d2" stroke-width="2"><rect x="5" y="5" width="20" height="20" stroke-dasharray="3 2"/><path d="M10 20l9-9M13 11h6v6"/></svg></div>Scalable</div>
</section>

<h2 class="abs sec-title" style="top:1882px">Our Partners</h2>
<div class="abs partner" style="left:150px;top:1964px"><i></i>Aveline</div>
<div class="abs partner" style="left:385px;top:1964px"><i></i>Norvik</div>
<div class="abs partner" style="left:610px;top:1964px"><i></i>Cirrusta</div>
<div class="abs partner" style="left:832px;top:1964px"><i></i>Rackmont</div>
<div class="abs partner" style="left:1055px;top:1964px"><i></i>Fishlane</div>

<div class="abs pub-art" role="img" aria-label="Three business people around a large cloud with a wifi symbol, magnifier and padlock"></div>
<div class="abs pub-bg"></div>
<section class="pub">
  <h2 class="abs">If you're using a public cloud now...</h2>
  <div class="abs copy">
    <p>You could be paying too much... Public cloud pricing structures have a habit of sneakily scaling up very quickly. With SCAAS, you'll always know what you're paying for your private cloud services.</p>
    <p>You're likely not getting the benefits of full functionality... Public cloud providers cannot adopt new innovations and functions as quickly and easily as the private cloud solutions you'll get from SCAAS.</p>
    <p>You'll be tied to the services your provider can provide... Public cloud providers will have a limited suite of products and services to offer you. A SCAAS private cloud has no such limitations</p>
  </div>
  <a class="abs btn btn-blue" href="#">Let's Talk</a>
</section>

<section class="abs diff">
  <h2 class="abs">The SCAAS Difference</h2>
  <ul class="abs">
    <li><svg width="14" height="14" viewBox="0 0 14 14" fill="none" stroke="#fff" stroke-width="1.3"><circle cx="7" cy="7" r="6"/><path d="M4 7h6M7.5 4.5L10 7l-2.5 2.5"/></svg>We'll quickly get to grips with what your organisation needs, and deliver it via our private cloud solutions.</li>
    <li><svg width="14" height="14" viewBox="0 0 14 14" fill="none" stroke="#fff" stroke-width="1.3"><circle cx="7" cy="7" r="6"/><path d="M4 7h6M7.5 4.5L10 7l-2.5 2.5"/></svg>Enjoy the ease of the public cloud, combined with the features, innovations and flexibility of the private cloud.</li>
    <li><svg width="14" height="14" viewBox="0 0 14 14" fill="none" stroke="#fff" stroke-width="1.3"><circle cx="7" cy="7" r="6"/><path d="M4 7h6M7.5 4.5L10 7l-2.5 2.5"/></svg>You can focus on your core business while we support you with a dedicated cloud infrastructure.</li>
    <li><svg width="14" height="14" viewBox="0 0 14 14" fill="none" stroke="#fff" stroke-width="1.3"><circle cx="7" cy="7" r="6"/><path d="M4 7h6M7.5 4.5L10 7l-2.5 2.5"/></svg>We'll create and deliver the launchpad that will take your business forward.</li>
    <li><svg width="14" height="14" viewBox="0 0 14 14" fill="none" stroke="#fff" stroke-width="1.3"><circle cx="7" cy="7" r="6"/><path d="M4 7h6M7.5 4.5L10 7l-2.5 2.5"/></svg>Get the benefits of your own cloud infrastructure and reduce your operational costs</li>
    <li><svg width="14" height="14" viewBox="0 0 14 14" fill="none" stroke="#fff" stroke-width="1.3"><circle cx="7" cy="7" r="6"/><path d="M4 7h6M7.5 4.5L10 7l-2.5 2.5"/></svg>Fast and easy computing, storage and network resources</li>
    <li><svg width="14" height="14" viewBox="0 0 14 14" fill="none" stroke="#fff" stroke-width="1.3"><circle cx="7" cy="7" r="6"/><path d="M4 7h6M7.5 4.5L10 7l-2.5 2.5"/></svg>Managed operations from private OpenStratus clouds and Kubrix</li>
    <li><svg width="14" height="14" viewBox="0 0 14 14" fill="none" stroke="#fff" stroke-width="1.3"><circle cx="7" cy="7" r="6"/><path d="M4 7h6M7.5 4.5L10 7l-2.5 2.5"/></svg>We'll support your growth and scale your cloud as you need it.</li>
  </ul>
  <div class="abs diff-art" role="img" aria-label="Isometric laptop uploading to a cloud above a stack of data servers"></div>
</section>

<h2 class="abs sec-title" style="top:3088px">What Our Client Says...</h2>

<div class="abs tcard" style="left:92px">
  <div class="q"><svg width="30" height="22" viewBox="0 0 30 22" fill="#fff"><path d="M0 22V12C0 5 4 1 11 0v5c-3 1-5 3-5 6h5v11zM17 22V12c0-7 4-11 11-12v5c-3 1-5 3-5 6h5v11z"/></svg></div>
  <p>Lorem Ipsum is simply dummy text of the printing and typesetting industry. Lorem Ipsum has been the industry's standard dummy text ever since the 1500s, when an unknown</p>
  <div class="who">Daniel Hart</div><div class="role">Leader Of Stratolift</div>
  <svg class="tail" width="28" height="28" viewBox="0 0 28 28"><path d="M0 0h28L4 26z" fill="#fff"/></svg>
</div>
<div class="abs tcard active" style="left:443px">
  <div class="q"><svg width="30" height="22" viewBox="0 0 30 22" fill="#fff"><path d="M0 22V12C0 5 4 1 11 0v5c-3 1-5 3-5 6h5v11zM17 22V12c0-7 4-11 11-12v5c-3 1-5 3-5 6h5v11z"/></svg></div>
  <p>Lorem Ipsum is simply dummy text of the printing and typesetting industry. Lorem Ipsum has been the industry's standard dummy text ever since the 1500s, when an unknown</p>
  <div class="who">Daniel Hart</div><div class="role">Leader Of Stratolift</div>
  <svg class="tail" width="28" height="28" viewBox="0 0 28 28"><path d="M0 0h28L4 26z" fill="#1f86d2"/></svg>
</div>
<div class="abs tcard" style="left:790px">
  <div class="q"><svg width="30" height="22" viewBox="0 0 30 22" fill="#fff"><path d="M0 22V12C0 5 4 1 11 0v5c-3 1-5 3-5 6h5v11zM17 22V12c0-7 4-11 11-12v5c-3 1-5 3-5 6h5v11z"/></svg></div>
  <p>Lorem Ipsum is simply dummy text of the printing and typesetting industry. Lorem Ipsum has been the industry's standard dummy text ever since the 1500s, when an unknown</p>
  <div class="who">Daniel Hart</div><div class="role">Leader Of Stratolift</div>
  <svg class="tail" width="28" height="28" viewBox="0 0 28 28"><path d="M0 0h28L4 26z" fill="#fff"/></svg>
</div>

<h2 class="abs sec-title" style="top:3563px">Get In Touch</h2>
<div class="abs footer-bg"></div>
<form class="abs form">
  <div class="lead">please submit your question or comment using this contact form.</div>
  <div class="field" style="left:55px;top:65px;width:233px">First Name*</div>
  <div class="field" style="left:312px;top:65px;width:233px">Last Name*</div>
  <div class="field" style="left:55px;top:120px;width:233px">Phone*</div>
  <div class="field" style="left:312px;top:120px;width:233px">E-mail*</div>
  <div class="field" style="left:55px;top:175px;width:490px;height:103px">Massage*</div>
  <span class="btn btn-white">Submit</span>
</form>

<footer>
  <div class="abs foot-brand"><div class="brand"><i></i>Stratolift</div></div>
  <p class="abs foot-about">Stratolift as a Service is here to help small businesses utilise the power of the cloud without complicated set-ups or scary price tags.</p>

  <div class="abs fhead" style="left:345px;top:4052px">Site Map</div>
  <div class="abs flinks" style="left:345px;top:4086px">Products<br>Solutions<br>Pricing<br>Resources<br>About</div>

  <div class="abs fhead" style="left:592px;top:4052px">Contact Us</div>
  <div class="abs contact-row" style="left:585px;top:4092px;width:240px">
    <svg width="16" height="18" viewBox="0 0 16 18" fill="none" stroke="#fff" stroke-width="1.4"><path d="M8 17s6-6 6-10A6 6 0 002 7c0 4 6 10 6 10z"/><circle cx="8" cy="7" r="2"/></svg>
    <span>123, lorem ipsum is simply dummy text.</span></div>
  <div class="abs contact-row" style="left:585px;top:4145px">
    <svg width="16" height="16" viewBox="0 0 16 16" fill="none" stroke="#fff" stroke-width="1.4"><path d="M3 1h3l1.5 4-2 1.2a9 9 0 004.3 4.3L11 8.5l4 1.5v3c0 1-1 2-2 2A12 12 0 011 3c0-1 1-2 2-2z"/></svg>
    <span>(123) 456 7890</span></div>
  <div class="abs contact-row" style="left:585px;top:4193px">
    <svg width="16" height="13" viewBox="0 0 16 13" fill="none" stroke="#fff" stroke-width="1.4"><rect x="1" y="1" width="14" height="11"/><path d="M1 1l7 6 7-6"/></svg>
    <span>info@stratoliftmail.com</span></div>

  <div class="abs fhead" style="left:865px;top:4052px">News Latter</div>
  <div class="abs" style="left:868px;top:4098px;font-size:11.5px;color:#fff">Sign Up Our Newsletter</div>
  <div class="abs news-in">E-mail</div>
  <div class="abs news-go"><svg width="16" height="16" viewBox="0 0 16 16" fill="#fff"><path d="M1 7L15 1 11 15 8 9z"/></svg></div>

  <div class="abs bottombar">© 2022 <b>Stratolift</b>. All Rights Reserved.
    <div class="social" aria-label="Social links"><span></span><span></span><span></span><span></span></div>
  </div>
</footer>

</body>
</html>
```